Brim Contractors

We are a group of people that doing a picking fruits like Oranges and grapes seasonal. We would like to have the colors " light black or black " back ground of the card. Thanks

Industry/Entity Type

Group

Contact Information for Business Card

Mob 0498213564 . Fax 03 5187 3940. P.O.Box 517 Tarrawong Vic 3461

```html
<!DOCTYPE html>
<html lang="en">
<head>
<meta charset="utf-8">
<title>Brim Contractors – Business Card</title>
<link rel="stylesheet" href="https://fonts.googleapis.com/css2?family=Open+Sans:ital,wght@0,400;0,600;0,700;1,400&display=swap">
<style>
  :root {
    --page-bg: #ecebe8;
    --card-bg: #1f1f1f;
    --leaf-green: #6cbf2e;
    --orange: #e07a22;
    --tag-orange: #f0a21c;
    --text-light: #f2f2f2;
    --shadow: rgba(0, 0, 0, 0.28);
  }
  * { margin: 0; padding: 0; box-sizing: border-box; }
  html, body {
    width: 1200px;
    height: 867px;
    overflow: hidden;
    background: var(--page-bg);
    font-family: "Open Sans", Arial, sans-serif;
  }
  .canvas {
    position: relative;
    width: 1200px;
    height: 867px;
  }
  .card {
    position: absolute;
    width: 540px;
    height: 310px;
    background: var(--card-bg);
    border-radius: 14px;
    box-shadow: 0 10px 24px var(--shadow);
  }
  .card--front { left: 70px; top: 90px; }
  .card--back { left: 590px; top: 467px; }

  /* Front */
  .front-identity {
    position: absolute;
    left: 60px;
    top: 120px;
    text-align: right;
    width: 250px;
  }
  .brand-name {
    color: var(--leaf-green);
    font-weight: 700;
    font-size: 27px;
    letter-spacing: -0.3px;
    line-height: 1.1;
  }
  .tagline {
    color: var(--tag-orange);
    font-style: italic;
    font-size: 18px;
    line-height: 1.3;
  }
  .brand-dot {
    position: absolute;
    left: 340px;
    top: 85px;
    width: 140px;
    height: 140px;
    border-radius: 50%;
    background: var(--orange);
  }

  /* Back */
  .back-identity {
    position: absolute;
    left: 40px;
    top: 70px;
    width: 240px;
    text-align: center;
  }
  .back-identity .brand-dot-small {
    display: block;
    margin: 0 auto 14px;
    width: 86px;
    height: 86px;
    border-radius: 50%;
    background: var(--orange);
  }
  .back-identity .brand-name { font-size: 23px; }
  .back-identity .tagline { font-size: 16px; }

  .contact {
    position: absolute;
    left: 318px;
    top: 92px;
    color: var(--text-light);
    font-size: 19px;
    line-height: 1.32;
    list-style: none;
  }
  .contact .label {
    color: var(--leaf-green);
    font-weight: 700;
  }
</style>
</head>
<body>
<main class="canvas">
  <section class="card card--front" aria-label="Business card front">
    <div class="front-identity">
      <p class="brand-name">Brim Contractors</p>
      <p class="tagline">picking fruits</p>
    </div>
    <span class="brand-dot" aria-hidden="true"></span>
  </section>

  <section class="card card--back" aria-label="Business card back">
    <div class="back-identity">
      <span class="brand-dot-small" aria-hidden="true"></span>
      <p class="brand-name">Brim Contractors</p>
      <p class="tagline">picking fruits</p>
    </div>
    <ul class="contact">
      <li><span class="label">Mob:</span> 0498213564</li>
      <li><span class="label">Fax:</span> 03 5187 3940</li>
      <li>P.O.Box 517 Tarrawong</li>
      <li>Vic 3461</li>
    </ul>
  </section>
</main>
</body>
</html>
```